Verpackungen für Glückskekse
Zielgruppe
Wir sind ein Produzent für regionale Glückskekse aus Niederbayern. Unsere Zielgruppe sind hauptsächlich Frauen zwischen 25 und 55, da unsere Glückskekse hauptsächlich als Gastgeschenke für Hochzeiten, Taufen und Geburtstage verwendet werden.
Aufgabenstellung
Das Vektor Design ist für eine Kartonbox in 12x12x12cm für 12 einzeln verpackte Glückskekse. Auf der Box und auf den Glückskeksen soll der Spruch 'Schön, dass du da bist' stehen.
Primär sollen die Glückskekse auf Hochzeiten eingesetzt werden, die im Boho/Beige-Weiß/Pampasgras Stil dekoriert sind.
Ich habe bereits einen ersten Entwurf, bin mir aber dabei noch nicht ganz sicher. Deshalb sollte der Vorschlag nur als Anhaltspunkt gesehen werden. Gerne auch eigene Ideen anbieten.

```html
<!DOCTYPE html>
<html lang="de">
<head>
<meta charset="utf-8">
<title>Schön, dass du da bist – Boxdesign</title>
<link rel="stylesheet" href="https://fonts.googleapis.com/css2?family=Mrs+Saint+Delafield&display=swap">
<style>
  :root {
    --page: #ffffff;
    --edge: #b9b9bc;
    --panel: #ddd6d3;
    --panel-line: #ffffff;
    --ink: #3a3d4a;
    --sage: rgba(120, 140, 124, 0.30);
    --slate: rgba(112, 128, 146, 0.28);
    --sand: rgba(190, 176, 162, 0.34);
    --mist: rgba(160, 172, 182, 0.22);
  }
  * { margin: 0; padding: 0; box-sizing: border-box; }
  html, body {
    width: 1200px;
    height: 2168px;
    overflow: hidden;
    background: var(--page);
  }
  .canvas {
    position: relative;
    width: 1200px;
    height: 2168px;
  }
  .box-face {
    position: absolute;
    left: 120px;
    top: 604px;
    width: 960px;
    height: 960px;
    border: 1.5px solid var(--edge);
    background: var(--page);
  }
  .botanical-wreath {
    position: absolute;
    inset: 0;
    background:
      radial-gradient(circle 120px at 250px 110px, var(--sage), transparent),
      radial-gradient(circle 100px at 440px 80px, var(--slate), transparent),
      radial-gradient(circle 100px at 600px 100px, var(--mist), transparent),
      radial-gradient(circle 110px at 730px 110px, var(--sand), transparent),
      radial-gradient(circle 110px at 830px 240px, var(--slate), transparent),
      radial-gradient(circle 100px at 845px 420px, var(--sand), transparent),
      radial-gradient(circle 110px at 850px 600px, var(--sage), transparent),
      radial-gradient(circle 100px at 840px 760px, var(--sand), transparent),
      radial-gradient(circle 110px at 770px 860px, var(--slate), transparent),
      radial-gradient(circle 100px at 620px 860px, var(--sage), transparent),
      radial-gradient(circle 100px at 470px 850px, var(--slate), transparent),
      radial-gradient(circle 100px at 300px 850px, var(--sand), transparent),
      radial-gradient(circle 100px at 150px 760px, var(--slate), transparent),
      radial-gradient(circle 110px at 130px 600px, var(--sand), transparent),
      radial-gradient(circle 110px at 130px 420px, var(--mist), transparent),
      radial-gradient(circle 100px at 150px 260px, var(--sage), transparent);
  }
  .message-panel {
    position: absolute;
    left: 196px;
    top: 167px;
    width: 560px;
    height: 613px;
    background: var(--panel);
  }
  .message-panel::after {
    content: "";
    position: absolute;
    inset: 9px;
    border: 3px solid var(--panel-line);
  }
  .greeting {
    position: absolute;
    inset: 0;
    font-family: "Mrs Saint Delafield", cursive;
    color: var(--ink);
    font-weight: 400;
    line-height: 1;
  }
  .greeting-first {
    position: absolute;
    left: 0;
    right: 0;
    top: 180px;
    text-align: center;
    padding-left: 40px;
    font-size: 150px;
  }
  .greeting-second {
    position: absolute;
    left: 0;
    right: 0;
    top: 320px;
    text-align: center;
    font-size: 120px;
    white-space: nowrap;
  }
</style>
</head>
<body>
  <main class="canvas">
    <section class="box-face">
      <div class="botanical-wreath" role="img" aria-label="Aquarell-Kranz aus Farnen, Eukalyptuszweigen, Gräsern und Beerenzweigen in Salbeigrün, Graublau und Beige rund um das Textfeld"></div>
      <div class="message-panel">
        <h1 class="greeting">
          <span class="greeting-first">Schön,</span>
          <span class="greeting-second">dass du da bist!</span>
        </h1>
      </div>
    </section>
  </main>
</body>
</html>
```